Hi,

The project is a 2 page design of a deal aggregator website, the deals grid page, and the dedicated deal page , the wireframe layout can be found on http://www.pricenook.co. Some things to consider:

1. We will keep the animation as is, i.e. when the user clicks on any of the deal, the deal details shows up in the other page
2. we definitely need to set a color palette
3. The header will reman always on top
4. We're using a technique called infinite scroll, so the footer is never visible

It's an interesting project with a different take on the ui of the deals presentation.

• i like the style of the following:
http://pinvoxa.com/shots/587210-Clock-Timer
http://pinvoxa.com/shots/640918-Bargoset
http://pinvoxa.com/shots/731064-Menu-Sketch

```html
<!DOCTYPE html>
<html lang="en">
<head>
<meta charset="utf-8">
<title>pricenook.co – Deals</title>
<link rel="stylesheet" href="https://fonts.googleapis.com/css2?family=Arimo:wght@400;700&family=Open+Sans:wght@400;700&display=swap">
<style>
:root{
  --page:#e6e6e6;
  --ink:#333;
  --logo:#555;
  --logo-faint:#ececec;
  --nav-dark:#2e2e2e;
  --nav-light:#4a4a4a;
  --red:#d02a2a;
  --red-dark:#a81515;
  --red-light:#e54545;
  --sub-dark:#2f2f2f;
  --sub-light:#4d4d4d;
  --white:#fff;
  --card-line:#d8d8d8;
  --overlay:#2b2b2b;
  --food-a:#d4582a;
  --food-b:#a8401f;
  --river-a:#4aa8e0;
  --river-b:#2a7cc4;
  --pool-a:#3f9bd8;
  --pool-b:#1f74c0;
}
*{margin:0;padding:0;box-sizing:border-box}
html,body{width:1200px;height:829px;overflow:hidden}
body{position:relative;background:var(--page);font-family:"Open Sans",Arial,sans-serif;color:var(--ink)}

.counter-band{position:absolute;left:0;top:0;width:1200px;height:48px;background:repeating-linear-gradient(45deg,#222 0 2px,#1a1a1a 2px 4px);overflow:hidden}
.counter-band span{position:absolute;top:-9px;white-space:nowrap;font-family:Arimo,Arial,sans-serif;font-size:57px;letter-spacing:0;line-height:1;color:transparent;background:linear-gradient(#fff,#bbb);-webkit-background-clip:text;background-clip:text}
.counter-label{left:68px}
.counter-total{left:660px}

.site-header{position:absolute;left:0;top:48px;width:1200px;height:82px;background:var(--white);overflow:hidden}
.brand-faint{position:absolute;left:60px;top:-8px;white-space:nowrap;font:700 118px/1 "Open Sans",sans-serif;letter-spacing:-5px;color:var(--logo-faint)}
.brand{position:absolute;left:66px;top:12px;white-space:nowrap;font:700 48px/1 "Open Sans",sans-serif;letter-spacing:-2px;color:var(--logo)}

.main-nav{position:absolute;left:710px;top:48px;width:444px;height:55px;background:linear-gradient(var(--nav-light),var(--nav-dark));border:1px solid #222;border-top:none;border-radius:0 0 6px 6px;display:flex;align-items:center;padding-left:16px}
.main-nav a{font:700 14px Arimo,Arial,sans-serif;color:var(--white);text-decoration:none;padding:0 10px;height:100%;display:flex;align-items:center;white-space:nowrap}
.main-nav a.active{height:36px;background:linear-gradient(#3a3a3a,#262626);border:2px solid #111;border-radius:4px;box-shadow:0 0 0 1px #666}
.main-nav .sep{border-left:1px solid #222;box-shadow:-1px 0 0 #5a5a5a;padding:0 12px}
.main-nav .gap{margin-left:36px}

.category-bar{position:absolute;left:0;top:130px;width:1200px;height:62px;background:linear-gradient(var(--red-light),var(--red) 45%,var(--red-dark) 50%,#b71b1b);display:flex;padding-left:66px}
.category-bar a{display:flex;align-items:center;gap:4px;padding:0 8px;font:700 14px Arimo,Arial,sans-serif;color:var(--white);text-decoration:none;white-space:nowrap;border-left:1px solid #8f1010;border-right:1px solid #e35b5b}
.category-bar svg{width:20px;height:18px;fill:var(--white)}

.sort-bar{position:absolute;left:0;top:192px;width:1200px;height:33px;background:linear-gradient(var(--sub-light),var(--sub-dark));display:flex;padding-left:66px}
.sort-bar a{position:relative;display:flex;align-items:center;gap:6px;padding:0 10px;font:700 14px Arimo,Arial,sans-serif;color:var(--white);text-decoration:none;white-space:nowrap;border-left:1px solid #222;border-right:1px solid #5e5e5e}
.sort-bar svg{width:16px;height:16px;fill:var(--white)}
.sort-bar a.current::after{content:"";position:absolute;left:36px;bottom:0;border:5px solid transparent;border-bottom-color:#ddd}

.deal{position:absolute;width:333px;background:var(--white);border:1px solid var(--card-line);border-radius:3px;box-shadow:0 1px 2px rgba(0,0,0,.12);overflow:hidden}
.deal h2{font:400 13px/17px "Open Sans",sans-serif;color:var(--ink);padding:5px 8px 0;height:60px}
.deal .photo{position:absolute;left:10px;top:60px;width:312px;height:218px}
.photo-food{background:linear-gradient(160deg,var(--food-a),var(--food-b))}
.photo-river{background:linear-gradient(160deg,var(--river-a),var(--river-b))}
.photo-pool{background:linear-gradient(160deg,var(--pool-a),var(--pool-b))}

.price-row{position:absolute;left:20px;top:218px;width:297px;display:flex;justify-content:space-between}
.price-row div{width:95px;height:49px;background:linear-gradient(var(--red-light),var(--red-dark));border:1px solid #8a1010;border-radius:3px;color:var(--white);font:400 13px/16px "Open Sans",sans-serif;text-align:center;padding-top:8px;text-transform:uppercase}

.deal-info{position:absolute;left:0;bottom:0;width:100%;height:75px;background:var(--overlay)}
.deal-info .zigzag{position:absolute;left:0;top:-8px;width:100%;height:9px}
.deal-info p{position:absolute;left:9px;color:var(--white);font:400 13px "Open Sans",sans-serif;display:flex;align-items:center;gap:6px;white-space:nowrap}
.deal-info svg{fill:var(--white)}
.time-tag{position:absolute;right:0;top:22px;width:107px;height:28px;background:var(--red);clip-path:polygon(0 0,100% 0,100% 100%,0 100%,8px 50%);color:var(--white);font:400 13px "Open Sans",sans-serif;display:flex;align-items:center;gap:6px;padding-left:20px;white-space:nowrap}
</style>
</head>
<body>

<div class="counter-band"><span class="counter-label">COUNTING</span><span class="counter-total">152 DEAL FOUND</span></div>

<header class="site-header">
  <div class="brand-faint" aria-hidden="true">pricenook.co</div>
  <div class="brand">pricenook.co</div>
</header>

<nav class="main-nav">
  <a class="active" href="#">Home</a>
  <a href="#">Widget</a>
  <a href="#">Nile Desks</a>
  <a class="sep gap" href="#">Contact</a>
  <a class="sep" href="#">Help</a>
</nav>

<nav class="category-bar">
  <a href="#"><svg viewBox="0 0 20 18"><path d="M6 2l-5 3 2 4 2-1v9h10V8l2 1 2-4-5-3c-1 2-5 2-8 0z"/></svg>Clothing</a>
  <a href="#"><svg viewBox="0 0 20 18"><path d="M1 2h18v11H1zM3 4v7h14V4zM7 14h6v2H7z"/></svg>Electronics</a>
  <a href="#"><svg viewBox="0 0 20 18"><path d="M10 1l9 8h-3v8h-4v-5H8v5H4V9H1z"/></svg>Home &amp; Office</a>
  <a href="#"><svg viewBox="0 0 20 18"><path d="M2 1h1v5h1V1h1v5h1V1h1v6l-2 1v9H4V8L2 7zM10 1h2v16h-2zM14 1c3 0 4 4 4 7h-2v9h-2z"/></svg>Eat &amp; Drink</a>
  <a href="#"><svg viewBox="0 0 20 18"><path d="M7 1h6v3h6v13H1V4h6zM9 3v1h2V3zM9 7v3H6v2h3v3h2v-3h3v-2h-3V7z"/></svg>Health &amp; Beauty</a>
  <a href="#"><svg viewBox="0 0 20 18"><path d="M7 2h6v3h6v11H1V5h6zM9 4v1h2V4zM1 9h18v1H1z"/></svg>Travel</a>
  <a href="#"><svg viewBox="0 0 20 18"><path d="M1 8h18v2h-1a4 4 0 0 1-7 0H9a4 4 0 0 1-7 0H1zM4 9a2 2 0 0 0 4 0zM12 9a2 2 0 0 0 4 0zM3 7l3-4h2L5 7zM17 7l-3-4h-2l3 4z"/></svg>Entertainment and Activities</a>
</nav>

<nav class="sort-bar">
  <a href="#"><svg viewBox="0 0 16 16"><path d="M1 1h7l7 7-7 7-7-7zM4 3a1 1 0 1 0 0 2 1 1 0 0 0 0-2z"/></svg>Discount</a>
  <a href="#">+ New</a>
  <a class="current" href="#"><svg viewBox="0 0 16 16"><path d="M8 1a7 7 0 1 0 0 14A7 7 0 0 0 8 1zM5 5h2v2H5zm4 0h2v2H9zM4 9h8a4 4 0 0 1-8 0z"/></svg>Populer</a>
  <a href="#"><svg viewBox="0 0 16 16"><path d="M3 5c2-3 8-3 10 0h2v4h-2l-1 4h-2v-2H6v2H4L3 10 1 9V6z"/></svg>Saving</a>
  <a href="#"><svg viewBox="0 0 16 16"><path d="M8 2a7 7 0 1 0 0 14A7 7 0 0 0 8 2zm0 2a5 5 0 1 1 0 10A5 5 0 0 1 8 4zM7 5h2v4H7zM6 0h4v1H6z"/></svg>Time Left</a>
</nav>

<article class="deal" style="left:93px;top:270px;height:288px">
  <h2>Verdello Cafe: Get a FREE E-Voucher and Enjoy 40% Discount on Delightful Italian Snacks and Drinks</h2>
  <div class="photo photo-food" role="img" aria-label="Photo of a pizza with peppers and olives"></div>
  <div class="deal-info">
    <svg class="zigzag" viewBox="0 0 333 9" preserveAspectRatio="none"><path fill="#2b2b2b" d="M0 9V0l10 8 10-8 10 8 10-8 10 8 10-8 10 8 10-8 10 8 10-8 10 8 10-8 10 8 10-8 10 8 10-8 10 8 10-8 10 8 10-8 10 8 10-8 10 8 10-8 10 8 10-8 10 8 10-8 10 8 10-8 10 8 10-8 10 8 3-2V9z"/></svg>
    <p style="top:15px"><svg width="18" height="14" viewBox="0 0 20 18"><path d="M2 1h1v5h1V1h1v5h1V1h1v6l-2 1v9H4V8L2 7zM10 1h2v16h-2zM14 1c3 0 4 4 4 7h-2v9h-2z"/></svg>Eat and Drink Offers</p>
    <p style="top:43px"><svg width="28" height="14" viewBox="0 0 28 14"><path d="M4 0l1 3h3L6 5l1 3-3-2-3 2 1-3-2-2h3zM14 0l1 3h3l-2 2 1 3-3-2-3 2 1-3-2-2h3zM9 6l1 3h3l-2 2 1 3-3-2-3 2 1-3-2-2h3z"/></svg>2525 bought this deal</p>
    <div class="time-tag"><svg width="14" height="14" viewBox="0 0 16 16"><path d="M8 2a7 7 0 1 0 0 14A7 7 0 0 0 8 2zm0 2a5 5 0 1 1 0 10A5 5 0 0 1 8 4zM7 5h2v4H7zM6 0h4v1H6z"/></svg>7 H 35 M</div>
  </div>
</article>

<article class="deal" style="left:445px;top:270px;height:288px">
  <h2>L.E 350 Instead of L.E 700 for a Romantic Dinner for Two and an Enchanting Private-Yacht Nile Cruise from River Orchid</h2>
  <div class="photo photo-river" role="img" aria-label="Photo of a white yacht on the river with city towers behind"></div>
  <div class="price-row"><div>Discount<br>50%</div><div>Value<br>700 LE</div><div>Price<br>350 LE</div></div>
</article>

<article class="deal" style="left:796px;top:270px;height:288px">
  <h2>EGP 50 Instead of EGP 100 for a Day Use and Delicious Lunch at the Amazing Al Warda Village</h2>
  <div class="photo photo-pool" role="img" aria-label="Photo of a resort swimming pool with palm trees and parasols"></div>
  <div class="price-row"><div>Discount<br>50%</div><div>Value<br>100 LE</div><div>Price<br>50 LE</div></div>
</article>

<article class="deal" style="left:93px;top:571px;height:300px">
  <h2>Verdello Cafe: Get a FREE E-Voucher and Enjoy 40% Discount on Delightful Italian Snacks and Drinks</h2>
  <div class="photo photo-food" role="img" aria-label="Photo of a pizza with peppers and olives"></div>
  <div class="price-row"><div>Discount<br>100%</div><div>Value<br>40 LE</div><div>Price<br>0 LE</div></div>
</article>

<article class="deal" style="left:445px;top:571px;height:300px">
  <h2>L.E 350 Instead of L.E 700 for a Romantic Dinner for Two and an Enchanting Private-Yacht Nile Cruise from River Orchid</h2>
  <div class="photo photo-river" role="img" aria-label="Photo of a white yacht on the river with city towers behind"></div>
  <div class="price-row"><div>Discount<br>50%</div><div>Value<br>700 LE</div><div>Price<br>350 LE</div></div>
</article>

<article class="deal" style="left:796px;top:571px;height:300px">
  <h2>EGP 50 Instead of EGP 100 for a Day Use and Delicious Lunch at the Amazing Al Warda Village</h2>
  <div class="photo photo-pool" role="img" aria-label="Photo of a resort swimming pool with palm trees and parasols"></div>
  <div class="price-row"><div>Discount<br>50%</div><div>Value<br>100 LE</div><div>Price<br>50 LE</div></div>
</article>

</body>
</html>
```